Home Accessibility

Steadfast Dwelling Builders (SDB) is a specialty construction company specializing in building custom homes and home modifications for individuals that are “Aging in Place” or with disabilities.
SDB is a full service construction company specializing in making independence accessible by helping people plan for now and the future. We provide a number of building services from custom designing a new home to modifying an existing home. SDB is a Licensed Residential Adaptation Expert (LRAE). As a LRAE specialist, SDB is able to offer specialized strategies and techniques for designing and building aesthetically enriching living environments.
Marcus has been in the building industry for over 18 years; He has served on the board of the Residential Framers Guild. He is Licensed Residential Adaptation Expert (LRAE). Certified, also as Eco Construction for Trade Practitioners and a member of the Fair Commerce Council (FCC)

I am looking for a promo piece where we install 2- 24" Kravo grab bars for $149.00
We can also do a free home evaluation which will show what or if any other modification or feature would be beneficial to them and the home.

Target Market(s)

Age 65+, disable, children of 65+

Industry/Entity Type

Construction

Requirements
Nice to have
• I would like to incorporate some or all of the bullet points from my mailer

```html
<!DOCTYPE html>
<html lang="en">
<head>
<meta charset="utf-8">
<title>Fall Prevention for Older Adults | Steadfast Dwelling Builders</title>
<link rel="stylesheet" href="https://fonts.googleapis.com/css2?family=Dancing+Script:wght@500;600&family=Lato:wght@400;700&display=swap">
<style>
  :root {
    --lime: #cfd755;
    --olive: #8d9a3c;
    --olive-band: #a2ad3f;
    --beige: #e8e7cf;
    --white: #ffffff;
    --ink: #262612;
    --script-ink: #4d4d1f;
    --photo-dark: #3f4a34;
    --photo-mid: #8a9185;
    --photo-light: #c9ccc4;
  }
  html, body {
    margin: 0;
    padding: 0;
    overflow: hidden;
    background: var(--lime);
  }
  .canvas {
    position: relative;
    width: 1200px;
    height: 930px;
    overflow: hidden;
    background: var(--lime);
    font-family: "Lato", sans-serif;
    color: var(--ink);
  }
  .header-art {
    position: absolute;
    left: 0;
    top: 0;
    width: 1200px;
    height: 400px;
    display: block;
  }
  .stat-callout {
    position: absolute;
    left: 380px;
    top: 36px;
    width: 440px;
    margin: 0;
    text-align: center;
    font-family: "Dancing Script", cursive;
    font-weight: 500;
    font-size: 38px;
    line-height: 46px;
    color: var(--script-ink);
  }
  .intro {
    position: absolute;
    left: 0;
    top: 483px;
    width: 1200px;
    margin: 0;
    text-align: center;
    font-size: 22.5px;
    line-height: 28px;
  }
  .question {
    position: absolute;
    left: 0;
    top: 614px;
    width: 1200px;
    margin: 0;
    text-align: center;
    font-family: "Dancing Script", cursive;
    font-weight: 600;
    font-size: 57px;
    line-height: 64px;
    color: var(--script-ink);
  }
  .tips {
    position: absolute;
    left: 0;
    top: 722px;
    width: 1200px;
    margin: 0;
    text-align: center;
    font-size: 23px;
    line-height: 28.5px;
  }
  .offer {
    position: absolute;
    left: 0;
    top: 854px;
    width: 1200px;
    margin: 0;
    text-align: center;
    font-size: 19px;
    line-height: 25px;
    color: var(--script-ink);
  }
  .offer strong {
    font-weight: 700;
  }
</style>
</head>
<body>
<main class="canvas">
  <svg class="header-art" viewBox="0 0 1200 400" xmlns="http://www.w3.org/2000/svg">
    <defs>
      <linearGradient id="photoTone" x1="0" y1="0" x2="0" y2="1">
        <stop offset="0" stop-color="var(--photo-dark)"/>
        <stop offset="0.45" stop-color="var(--photo-mid)"/>
        <stop offset="1" stop-color="var(--photo-light)"/>
      </linearGradient>
    </defs>

    <g role="img" aria-label="Photo of older adults doing balance exercises outdoors with arms outstretched">
      <path d="M0 0 H412 C398 100 398 200 412 320 H0 Z" fill="url(#photoTone)"/>
    </g>
    <g role="img" aria-label="Mirrored photo of older adults doing balance exercises outdoors">
      <path d="M1200 0 H808 C822 100 822 200 808 320 H1200 Z" fill="url(#photoTone)"/>
    </g>

    <path class="stat-panel" d="M396 0 H824 C806 90 800 200 812 320 H408 C420 200 414 90 396 0 Z" fill="var(--olive)"/>
    <path d="M394 0 H406 C424 90 430 200 418 320 H404 C416 200 410 90 394 0 Z" fill="var(--white)"/>
    <path d="M814 0 H826 C808 90 802 200 814 320 H800 C788 200 796 90 814 0 Z" fill="var(--white)"/>

    <path class="band-olive" d="M0 300 C200 285 420 335 620 330 C820 325 1000 280 1200 300 V395 C1000 375 800 385 600 390 C400 395 200 365 0 392 Z" fill="var(--olive-band)"/>
    <path class="band-beige" d="M0 262 C250 258 450 322 650 306 C850 290 1000 250 1200 258 V338 C1000 322 850 326 650 344 C450 360 250 310 0 312 Z" fill="var(--beige)"/>
    <path class="band-white" d="M0 212 C140 200 280 236 412 258 C600 290 820 268 1000 222 C1080 205 1150 205 1200 214 V262 C1000 254 850 292 650 308 C450 324 250 262 0 266 Z" fill="var(--white)"/>
  </svg>

  <p class="stat-callout">Each year, one<br>in every three adults<br>age 65 and older falls.</p>

  <p class="intro">Falls can cause moderate to severe injuries, such as hip fractures and head traumas,<br>and can increase the risk of early death.<br>Fortunately, falls are a public health problem that is largely preventable.</p>

  <h1 class="question">How can older adults prevent falls?</h1>

  <p class="tips">Older adults can stay independent and reduce their chances of falling by;<br>Make homes safer by reducing tripping hazards,<br>adding grab bars inside and outside the tub or shower and next to the toilet,<br>adding railings on both sides of stairways, and improving the lighting in homes.</p>

  <p class="offer"><strong>Steadfast Dwelling Builders (SDB)</strong> installs two 24" Kravo grab bars for just <strong>$149.00</strong><br>Ask about our free home evaluation with a Licensed Residential Adaptation Expert (LRAE)</p>
</main>
</body>
</html>
```